Consulting Firm Proposal Template

We need a template for proposals that we send to our clients using the attached outline. Our company is "Brindlemere Consulting Group". We would like a title page with the rest of the information on the following pages. The title page and subsequent pages should be designed in a way to support the use of pictures or graphics. We are looking to use a bold black and white color scheme. Overall we would like the design to confirm our deep experience and knowledge while still following modern design trends.

Target Market(s)

Medium Size Corporations

Industry/Entity Type

Consulting

Logo Text

Brindlemere Consulting Group

Font styles to use
Serif
Sans Serif

Colors

Designer to choose only greyscale colors for use in the design.

Requirements
Must have
• Title Page
Headers
Footers

```html
<!DOCTYPE html>
<html lang="en">
<head>
<meta charset="utf-8">
<title>Brindlemere Consulting Group – Proposal Cover</title>
<link rel="stylesheet" href="https://fonts.googleapis.com/css2?family=Playfair+Display:wght@500&family=Roboto:wght@300&display=swap">
<style>
  :root {
    --canvas-bg: #f4f4f4;
    --cover-black: #121212;
    --text-light: #e6e6e6;
    --band-light: #e9e9e9;
    --band-mid: #a8a8a8;
    --band-dark: #3a3a3a;
  }
  * { margin: 0; padding: 0; box-sizing: border-box; }
  html, body {
    width: 1200px;
    height: 1000px;
    overflow: hidden;
    background: var(--canvas-bg);
  }
  .canvas {
    position: relative;
    width: 1200px;
    height: 1000px;
  }
  .cover {
    position: absolute;
    left: 260px;
    top: 63px;
    width: 680px;
    height: 874px;
    background: var(--cover-black);
    box-shadow: 0 10px 30px rgba(0, 0, 0, 0.25);
  }
  .cover-visual {
    position: absolute;
    left: 0;
    top: 115px;
    width: 100%;
    height: 285px;
    background:
      linear-gradient(180deg, rgba(255,255,255,0.15) 0%, rgba(0,0,0,0) 40%, rgba(0,0,0,0.35) 100%),
      linear-gradient(90deg, var(--band-dark) 0%, var(--band-mid) 22%, var(--band-light) 45%, var(--band-mid) 70%, var(--band-dark) 100%);
  }
  .cover-identity {
    position: absolute;
    right: 40px;
    top: 520px;
    text-align: right;
    color: var(--text-light);
  }
  .company-name {
    font-family: "Playfair Display", Georgia, serif;
    font-weight: 500;
    font-size: 29px;
    letter-spacing: -0.4px;
    line-height: 1.2;
    margin-bottom: 40px;
  }
  .contact-list {
    list-style: none;
    font-family: "Roboto", Arial, sans-serif;
    font-weight: 300;
    font-size: 13.5px;
    line-height: 19.5px;
  }
</style>
</head>
<body>
  <main class="canvas">
    <section class="cover">
      <div class="cover-visual" role="img" aria-label="Black and white double-exposure photograph of business people shaking hands layered over a city skyline"></div>
      <div class="cover-identity">
        <h1 class="company-name">Brindlemere Consulting Group</h1>
        <ul class="contact-list">
          <li>18 Harlow Crescent Millbrook,</li>
          <li>NJ 08190</li>
          <li>+001 02 555 418</li>
          <li>www.brindlemere.com</li>
          <li>hello@brindlemere.com</li>
        </ul>
      </div>
    </section>
  </main>
</body>
</html>
```